1. 商品のコンセプト:鉢植えの植物を元気にみずみずしく保つ。お客様に代わって心を込めたお手入れを。
2. 商品コンセプトの理由:水やり以外のお手入れは放置しがちな鉢植えも、お手入れすることで美しく保てることで、安らぎや楽しみを与えてくれる存在となります。
3. 販売価格:(価格はすべて税込み)
【植替え】
新しく植え替える鉢の上部直径
15㎝(5号鉢)まで 3,500円
21㎝(7号鉢)まで 6,000円
30㎝(10号鉢)まで 9,000円
45㎝(15号鉢)まで 15,000円
※ただし、盆栽は除く
●料金は作業代のみの価格となります。
●植替えで必要な鉢や土などは、お客さまがご用意いただければ別途費用がかからず、そちらを使用して作業致します。
ただし、樹種や状態によって必要な鉢のサイズや土の種類や量がありますので、お見積り時にご相談のうえご用意いただけるのが望ましいです。
●また、鉢や土など当社でご用意することも可能です。その場合、別途お見積りとなります。
●古い土は、ご希望があればお引き取りいたします(別途見積り)
●不要になった鉢のお引き取りは、ご相談ください(別途見積り)
※ただし、プラスチック、金属、ガラス、樹脂、コンクリートなどはお引き取りできません。
【剪定】形を整えたり、高さを調整したりします。
高さ3m未満 4,000円/本
【消毒】病害虫の症状にあわせた薬剤は散布し予防や駆除をします。
高さ3m未満 2,000円/本
【施肥】肥料を施して栄養分を補い、成育促進、花付き、実付きの改善をします。
3,000円より
4. 販売方法
お見積り無料
ご依頼(電話・WEB)→担当から連絡→無料見積り(お客様宅へ出向いて実際のものを見てお見積りをします。見積書有効期限1か月)→ご依頼(作業日時決定)→作業→お支払い(郵便局・銀行から振り込み、コンビニエンスストアでのお支払い(コンビニ後払い)、クレジットカード決済)

[強み]
1鉢からでも承ります。お見積り無料。お客さまご自身で植替えに必要な鉢や土などを担当者にご相談のうえご用意いただけたら、費用は作業代のみとなります(土やゴミの回収ご希望の場合は別途費用がかかります)
社名、ロゴ、電話番号、URL、QRコード
A4
両面
緑系、水色系、茶系、こだわりはそれ程強くないので、色合いはお任せします。
• イラストレーター形式 (.ai)
弊社HP
https://www.375m.co.jp/
各種メニューと価格
https://www.375m.co.jp/price/

鉢植えの植替えや鉢植えのお手入れに関する素材については、フリー素材等にて適宜入れてください。
必要に応じてリクエストさせていただきたいと思います。

必要な情報が一通り網羅されていました。
シンプルに当社のサービスを表現されていました。

短期間の中多くのご提案をいただき、誠にありがとうございました。
どのご提案もレベルが高く、良い意味で選定に苦慮しました。
また新たなチラシ作成の際は是非ご提案いただければ幸いです。

```html
<!DOCTYPE html>
<html lang="ja">
<head>
<meta charset="utf-8">
<title>みどり庭舎 鉢植えのお手入れ</title>
<link rel="stylesheet" href="https://fonts.googleapis.com/css2?family=M+PLUS+Rounded+1c:wght@500;700;800&family=Noto+Sans+JP:wght@400;700&display=swap">
<style>
:root{
  --sky-top:#e3f4fb;
  --sky-bottom:#ffffff;
  --green:#5aab3a;
  --green-dark:#2f7d2c;
  --leaf-light:#e4f3c9;
  --leaf-mid:#b9dc84;
  --orange:#f08c00;
  --red:#e60012;
  --brown:#a65628;
  --brown-dark:#7c3915;
  --text:#333333;
  --white:#ffffff;
}
*{margin:0;padding:0;box-sizing:border-box}
html,body{width:849px;height:1200px;overflow:hidden}
body{font-family:"M PLUS Rounded 1c","Noto Sans JP",sans-serif;color:var(--text)}
.flyer{position:relative;width:849px;height:1200px;background:linear-gradient(180deg,var(--sky-top) 0%,var(--sky-bottom) 55%,var(--sky-top) 100%);overflow:hidden}
.header{position:absolute;left:0;top:0;width:849px;height:100px;border-bottom:3px solid var(--green)}
.brand{position:absolute;left:30px;top:26px;display:flex;align-items:center;gap:10px}
.brand-dot{width:22px;height:22px;border-radius:50%;background:var(--green)}
.brand-name{font-size:34px;font-weight:800;color:var(--green-dark);letter-spacing:2px}
.header-question{position:absolute;left:345px;top:30px;width:475px;height:50px;border:3px solid var(--green);border-radius:10px;background:var(--white);font-size:22px;font-weight:700;color:var(--green-dark);display:flex;align-items:center;justify-content:center}
.headline{position:absolute;color:var(--orange);font-weight:800;font-size:46px;text-shadow:3px 3px 0 var(--white),-3px -3px 0 var(--white),3px -3px 0 var(--white),-3px 3px 0 var(--white);letter-spacing:2px}
.headline-1{left:180px;top:130px}
.headline-2{left:345px;top:195px}
.plant-art{position:absolute;left:60px;top:270px;width:740px;height:880px;border-radius:24px;background:linear-gradient(180deg,var(--leaf-light) 0%,var(--leaf-mid) 52%,var(--brown-dark) 56%,var(--brown) 62%,var(--brown) 100%)}
.menu{position:absolute;text-align:center;color:var(--text)}
.menu-title{font-size:40px;font-weight:800;color:var(--green-dark);text-shadow:2px 2px 0 var(--white),-2px -2px 0 var(--white),2px -2px 0 var(--white),-2px 2px 0 var(--white)}
.menu-line{font-size:22px;font-weight:700}
.menu-price{font-size:30px;font-weight:800}
.menu-price small{font-size:18px}
.menu-note{font-size:10px;line-height:1.4;text-align:left;font-family:"Noto Sans JP",sans-serif;font-weight:400}
.menu-repot{left:90px;top:290px;width:310px}
.menu-repot .menu-title{font-size:44px}
.menu-repot .exclude{position:absolute;left:238px;top:20px;font-size:10px;font-weight:500}
.menu-repot .menu-line{font-size:21px;line-height:1.5;margin-top:4px}
.menu-repot .menu-note{margin:14px auto 0;width:240px}
.menu-prune{left:560px;top:320px;width:230px}
.menu-disinfect{left:570px;top:525px;width:225px}
.menu-fertilize{left:250px;top:590px;width:190px}
.banner{position:absolute;left:28px;top:860px;width:750px;height:92px;background:var(--white);border-radius:14px;display:flex;align-items:baseline;justify-content:center;padding-top:10px;font-weight:800;font-size:44px;color:var(--text)}
.banner-count{color:var(--red);font-size:64px;text-decoration:underline;text-decoration-thickness:4px;text-underline-offset:6px}
.estimate{position:absolute;left:255px;top:975px;width:340px;height:66px;background:var(--green);border-radius:33px;display:flex;align-items:center;justify-content:center;gap:14px;color:var(--white);font-size:28px;font-weight:800}
.estimate-free{background:var(--white);color:var(--red);border-radius:8px;padding:0 12px;font-size:34px}
.tax-note{position:absolute;left:18px;top:1170px;font-size:11px;font-family:"Noto Sans JP",sans-serif;color:var(--text)}
.more{position:absolute;left:605px;top:1140px;width:225px;height:46px;background:var(--white);border:2px solid var(--green);border-radius:8px;display:flex;align-items:center;justify-content:center;font-size:21px;font-weight:700;color:var(--text)}
</style>
</head>
<body>
<div class="flyer">
  <header class="header">
    <div class="brand"><span class="brand-dot"></span><span class="brand-name">みどり庭舎</span></div>
    <div class="header-question">鉢植え植物のお困りごとありませんか？</div>
  </header>

  <p class="headline headline-1">鉢植えのお手入れなら</p>
  <p class="headline headline-2">お任せください！</p>

  <div class="plant-art" role="img" aria-label="茶色の植木鉢から伸びる木の枝と、メニューを載せた丸い葉のイラスト"></div>

  <section class="menu menu-repot">
    <h2 class="menu-title">鉢替え</h2>
    <span class="exclude">※盆栽は除く</span>
    <p class="menu-line">小さい鉢から<br>４５cm（15号鉢）まで<br>様々なサイズに対応いたします</p>
    <p class="menu-price">3,500円<small>より</small></p>
    <p class="menu-note">・鉢と土をご用意いただければ費用は作業代のみ<br>・古い土や鉢の引き取りは別途お見積りとなります</p>
  </section>

  <section class="menu menu-prune">
    <h2 class="menu-title">剪定</h2>
    <p class="menu-line">高さ３ｍ未満</p>
    <p class="menu-price">4,000<small>円/本</small></p>
  </section>

  <section class="menu menu-disinfect">
    <h2 class="menu-title">消毒</h2>
    <p class="menu-line">高さ３ｍ未満</p>
    <p class="menu-price">2,000<small>円/本</small></p>
  </section>

  <section class="menu menu-fertilize">
    <h2 class="menu-title">施肥</h2>
    <p class="menu-price">3,000<small>円より</small></p>
  </section>

  <div class="banner"><span class="banner-count">1鉢</span>からでも承ります!</div>
  <div class="estimate"><span>お見積もり</span><span class="estimate-free">無料!</span></div>

  <p class="tax-note">表示価格は全て税込みです。</p>
  <div class="more">くわしくは裏面へ！</div>
</div>
</body>
</html>
```